Book cover needed for Christian Non-Fiction Book

I need book cover design (eBook , Paperback, and possibly case laminate Hardcover) for use on PQL and Halvet Print.
Title: Go Forth Called
Sub-Title: Leaving Shelter and Walking in Faithful Purpose
Author: Owen Callery
Also on front cover "Forward by R. Lisel Marrow"

I like clean/simple designs. Below are links to examples of covers I like...
https://www.bookvantle.example/dp/X4821QPT7M?tag=plumwick-20&linkCode=ogi&th=1&psc=1
https://www.bookvantle.example/dp/X49KTRMWHZ?tag=plumwick-20&linkCode=ogi&th=1&psc=1
https://www.bookvantle.example/dp/X22HQC51NT?tag=plumwick-20&linkCode=ogi&th=1&psc=1
https://www.bookvantle.example/dp/X48F3WZPDR?tag=plumwick-20&linkCode=ogi&th=1&psc=1
https://www.bookvantle.example/dp/X4M7UVVCLE?tag=plumwick-20&linkCode=ogi&th=1&psc=1
https://www.bookvantle.example/dp/X2R9HNNKA6?tag=plumwick-20&linkCode=ogi&th=1&psc=1

The main idea for Go Forth Called is that God is a sending God and being "on the move" or journeying is central to God's character, and therefore God's people. I write about our hesitancy to "go," and how the Bible is full of stories about people "going" from Abraham to Jesus, to the disciples of Jesus.

The core biblical text is the Great Commission in Matthew 28:16-20, where Jesus sends out his followers, though some of them doubt.

This paragraph from the forward by R. Lisel Marrow captures the tone of the book well:
This book is a call amid the turmoil. Sacred scripture contains no shortage of narratives in which humans are pulled from their ordinary lives with an inciting incident whose stakes are high. These Biblical figures are lulled from complacency and comfort zones—and yet they are reluctant to serve because they question their ability and influence. Their lessons are relevant for us today: They, and we, are always called and sent with authority. The power of the Holy Spirit equips their “going”—and ours. It’s a sending out that looks less like mastery and more humility. It’s a sending out that is unequivocal service to others modelled in a rabbi-reformer who washed feet and touched the unclean.

I have previously published two shorter books and would be very interested in getting new covers for the old books these so that the three have a similar feel. Whichever designer I go with for "Go Forth Called" I would also want to work with on creating a "branded look" for the other two books.

Target Market(s)

Christian, Religion, Spirituality Readers

Requirements
Must have
• The front cover must have this copy...
Go Forth Called
Leaving Shelter and Walking in Faithful Purpose
Owen Callery
Forward by R. Lisel Marrow

Must be willing to do the full paperback and/or hardcover, but start with thefront cover please
Nice to have
• See attached files for some book covers I like

```html
<!DOCTYPE html>
<html lang="en">
<head>
<meta charset="utf-8">
<title>Go Forth Called — Front Cover</title>
<link rel="stylesheet" href="https://fonts.googleapis.com/css2?family=Cinzel:wght@400;500&family=Montserrat:wght@400&display=swap">
<style>
  :root {
    --page-bg: #e6e6e6;
    --sky-bright: #fbd35a;
    --sky-gold: #eea232;
    --sky-amber: #c8661c;
    --land-rust: #8a3a14;
    --earth-dark: #3a1206;
    --night: #0b0302;
    --title-ink: #0d0805;
    --light-ink: #f3ece4;
  }
  * { box-sizing: border-box; margin: 0; padding: 0; }
  html, body {
    width: 1200px; height: 800px; overflow: hidden;
    background: var(--page-bg);
  }
  .canvas {
    width: 1200px; height: 800px;
    display: flex; align-items: center; justify-content: center;
  }
  .cover {
    position: relative;
    width: 500px; height: 764px;
    overflow: hidden;
    border-radius: 3px;
  }
  .cover-art {
    position: absolute; inset: 0;
    width: 100%; height: 100%;
    display: block;
  }
  .title {
    position: absolute; left: 0; right: 0; top: 100px;
    font-family: "Cinzel", serif;
    font-weight: 500;
    color: var(--title-ink);
    text-align: center;
    font-size: 84px;
    line-height: 104px;
    letter-spacing: 2px;
  }
  .title span { display: block; }
  .subtitle {
    position: absolute; left: 0; right: 0; top: 554px;
    font-family: "Cinzel", serif;
    font-weight: 400;
    color: var(--light-ink);
    text-align: center;
    font-size: 19px;
    line-height: 26px;
    letter-spacing: 1.5px;
  }
  .author {
    position: absolute; left: 0; right: 0; top: 672px;
    font-family: "Montserrat", sans-serif;
    font-weight: 400;
    color: var(--light-ink);
    text-align: center;
    font-size: 25px;
    letter-spacing: 4px;
    text-transform: uppercase;
  }
  .foreword {
    position: absolute; left: 0; right: 0; top: 716px;
    font-family: "Cinzel", serif;
    font-weight: 400;
    color: var(--light-ink);
    text-align: center;
    font-size: 14px;
    letter-spacing: 2px;
  }
</style>
</head>
<body>
<main class="canvas">
  <section class="cover">
    <svg class="cover-art" viewBox="0 0 500 764" preserveAspectRatio="none" role="img"
         aria-label="Photograph of a golden sunset sky over hazy mountains, a man kneeling in prayer on a glowing plain, fading to dark earth below">
      <defs>
        <linearGradient id="sky" x1="0" y1="0" x2="0" y2="1">
          <stop offset="0" stop-color="#d97a24"/>
          <stop offset="0.22" stop-color="var(--sky-gold)"/>
          <stop offset="0.42" stop-color="var(--sky-amber)"/>
          <stop offset="0.58" stop-color="#a24d1c"/>
          <stop offset="0.66" stop-color="#c47a3a"/>
          <stop offset="0.72" stop-color="var(--land-rust)"/>
          <stop offset="0.8" stop-color="var(--earth-dark)"/>
          <stop offset="0.9" stop-color="var(--night)"/>
          <stop offset="1" stop-color="var(--night)"/>
        </linearGradient>
        <radialGradient id="sun" cx="0.82" cy="0.22" r="0.45">
          <stop offset="0" stop-color="var(--sky-bright)" stop-opacity="0.95"/>
          <stop offset="0.5" stop-color="var(--sky-bright)" stop-opacity="0.35"/>
          <stop offset="1" stop-color="var(--sky-bright)" stop-opacity="0"/>
        </radialGradient>
      </defs>
      <rect width="500" height="764" fill="url(#sky)"/>
      <rect width="500" height="764" fill="url(#sun)"/>
    </svg>

    <h1 class="title">
      <span>Go</span>
      <span>Forth</span>
      <span>Called</span>
    </h1>
    <p class="subtitle">Leaving Shelter and Walking<br>in Faithful Purpose</p>
    <p class="author">Owen Callery</p>
    <p class="foreword">Forward by R. Lisel Marrow</p>
  </section>
</main>
</body>
</html>
```